business card with logo Marigold Nails & Spa 2815 SW Harlow Ave Portland OR 97099

Would like to have a business card with our logo.
like bottle of polish with our logo or letter M on it
want something that first glance would let you know that it is a nail salon.
like the hands with polish bottle dripping.
like black or White back ground

Marigold Nails & Spa
(The Velvet Retreat)
2815 SW Harlow Ave
Portland, OR 97099
Call or Text: 1-555-714-3928
www.MarigoldNailsnSpa.example
Open 7 days a week.
After 7:00 PM is by appointment only.
Closed only on Thanksgiving & Christmas.

Target Market(s)

20%Man and 80%Woman 13-70

Industry/Entity Type

Business

Contact Information for Business Card

Elegant with Logo-Business name- address-phone-open days. closed day.

Font styles to use
Decorative
Script

Colors
000000

Requirements
Must have
• Logo and place for Technician Name
• Marigold Nails & Spa
• (The Velvet Retreat)
• 2815 SW Harlow Ave
• Portland, OR 97099
• Call or Text: 1-555-714-3928
• Open 7 days a week
• Closed only on Thanksgiving & Christmas.
• We accepted all major credit cards but prefer cash. Thank you
Nice to have
• Nail polish bottle with our Logo or letter M
Should not have
• too colorful

```html
<!DOCTYPE html>
<html lang="en">
<head>
<meta charset="utf-8">
<title>Marigold Nails &amp; Spa – Business Card</title>
<link href="https://fonts.googleapis.com/css2?family=Lato:wght@400;700&display=swap" rel="stylesheet">
<style>
  :root {
    --stage: #2b2b2b;
    --card-light: #ffffff;
    --card-light-edge: #e6e6e6;
    --card-dark: #2a2a2a;
    --card-dark-edge: #141414;
    --ink: #1c1c1c;
    --ink-soft: #555555;
    --ink-light: #f2f2f2;
    --ink-light-soft: #bdbdbd;
    --accent-red: #c8211f;
    --accent-green: #a4c639;
    --photo-top: #f4f1ef;
    --photo-mid: #e9c9bd;
    --photo-red: #b8201c;
    --badge-one: #eeeeee;
    --badge-two: #3a6fb0;
    --badge-three: #4a9ad6;
    --badge-four: #e6e6e6;
  }
  html, body {
    margin: 0;
    padding: 0;
    width: 1200px;
    height: 1200px;
    overflow: hidden;
    background: var(--stage);
    font-family: "Lato", sans-serif;
  }
  .canvas {
    position: relative;
    width: 1200px;
    height: 1200px;
  }
  .card {
    position: absolute;
    top: 190px;
    width: 500px;
    height: 820px;
    border-radius: 22px;
    overflow: hidden;
    box-sizing: border-box;
  }

  /* Front */
  .card--front {
    left: 75px;
    background: radial-gradient(circle at 60% 45%, var(--card-light) 0%, var(--card-light) 45%, var(--card-light-edge) 100%);
    color: var(--ink);
  }
  .front__photo {
    position: absolute;
    top: 0;
    right: 25px;
    width: 195px;
    height: 550px;
    background: linear-gradient(180deg, var(--photo-top) 0%, var(--photo-mid) 30%, var(--photo-top) 55%, var(--photo-red) 80%, var(--photo-top) 100%);
    border-radius: 0 0 12px 12px;
  }
  .front__logo {
    position: absolute;
    top: 275px;
    left: 60px;
    width: 205px;
  }
  .logo-line {
    display: flex;
    align-items: center;
    gap: 10px;
  }
  .logo-dot {
    flex: none;
    width: 12px;
    height: 12px;
    border-radius: 50%;
    background: var(--accent-red);
  }
  .logo-name {
    font-size: 28px;
    font-weight: 700;
    color: var(--ink);
    line-height: 1.15;
  }
  .logo-tagline {
    margin: 8px 0 0 22px;
    font-size: 16px;
    color: var(--ink-soft);
  }
  .front__technician {
    position: absolute;
    left: 72px;
    right: 60px;
    top: 582px;
    display: flex;
    align-items: flex-end;
    gap: 10px;
    font-size: 18px;
  }
  .technician__line {
    flex: 1;
    border-bottom: 1px solid var(--ink-soft);
    height: 18px;
  }
  .front__contact {
    position: absolute;
    left: 72px;
    top: 640px;
    font-size: 20px;
    line-height: 1.3;
  }
  .contact-row {
    display: flex;
    align-items: flex-start;
    gap: 10px;
    margin-bottom: 14px;
  }
  .contact-row svg { flex: none; margin-top: 3px; }
  .contact-row--web { font-size: 19px; }

  /* Back */
  .card--back {
    left: 625px;
    background: radial-gradient(circle at 50% 30%, var(--card-dark) 0%, var(--card-dark-edge) 100%);
    color: var(--ink-light);
    text-align: center;
  }
  .back__logo {
    position: absolute;
    top: 165px;
    left: 0;
    right: 0;
    display: flex;
    justify-content: center;
    align-items: center;
    gap: 14px;
  }
  .back__logo .logo-name {
    color: var(--ink-light);
    font-size: 42px;
  }
  .back__logo .logo-dot { width: 16px; height: 16px; }
  .back__tagline {
    position: absolute;
    top: 228px;
    left: 0;
    right: 0;
    font-size: 20px;
    color: var(--ink-light-soft);
  }
  .back__hours {
    position: absolute;
    top: 495px;
    left: 0;
    right: 0;
    font-size: 21px;
    line-height: 1.6;
  }
  .back__cards-label {
    position: absolute;
    top: 615px;
    left: 0;
    right: 0;
    font-size: 21px;
    color: var(--accent-green);
  }
  .back__badges {
    position: absolute;
    top: 665px;
    left: 0;
    right: 0;
    display: flex;
    justify-content: center;
    gap: 18px;
  }
  .badge {
    width: 88px;
    height: 56px;
    border-radius: 7px;
  }
  .badge--one { background: var(--badge-one); }
  .badge--two { background: var(--badge-two); }
  .badge--three { background: var(--badge-three); }
  .badge--four { background: var(--badge-four); }
  .back__cash-note {
    position: absolute;
    top: 748px;
    left: 0;
    right: 0;
    font-size: 18px;
    color: var(--ink-light-soft);
  }
</style>
</head>
<body>
<main class="canvas">

  <section class="card card--front">
    <div class="front__photo" role="img" aria-label="Photo of a hand with red nails lifting a brush from a red nail polish bottle, polish dripping"></div>

    <div class="front__logo">
      <div class="logo-line">
        <span class="logo-dot"></span>
        <span class="logo-name">Marigold<br>Nails n Spa</span>
      </div>
      <div class="logo-tagline">(The Velvet Retreat)</div>
    </div>

    <div class="front__technician">
      <span>Technician:</span>
      <span class="technician__line"></span>
    </div>

    <div class="front__contact">
      <div class="contact-row">
        <svg width="16" height="22" viewBox="0 0 16 22" aria-hidden="true"><path d="M8 0C3.6 0 0 3.5 0 7.8 0 13.5 8 22 8 22s8-8.5 8-14.2C16 3.5 12.4 0 8 0zm0 11a3.2 3.2 0 1 1 0-6.4A3.2 3.2 0 0 1 8 11z" fill="#c8211f"/></svg>
        <div>2815 SW Harlow Ave<br>Portland, OR 97099</div>
      </div>
      <div class="contact-row">
        <svg width="14" height="22" viewBox="0 0 14 22" aria-hidden="true"><rect x="1" y="1" width="12" height="20" rx="2" fill="none" stroke="#c8211f" stroke-width="2"/><circle cx="7" cy="17" r="1.3" fill="#c8211f"/></svg>
        <div>1-555-714-3928(Call or Text)</div>
      </div>
      <div class="contact-row contact-row--web">
        <svg width="18" height="18" viewBox="0 0 18 18" aria-hidden="true"><g fill="none" stroke="#c8211f" stroke-width="1.5"><circle cx="9" cy="9" r="7.5"/><ellipse cx="9" cy="9" rx="3.5" ry="7.5"/><path d="M1.5 9h15M3 5h12M3 13h12"/></g></svg>
        <div>www.MarigoldNailsnSpa.example</div>
      </div>
    </div>
  </section>

  <section class="card card--back">
    <div class="back__logo">
      <span class="logo-dot"></span>
      <span class="logo-name">Marigold Nails n Spa</span>
    </div>
    <div class="back__tagline">(The Velvet Retreat)</div>

    <div class="back__hours">
      Open 7 days a week.<br>
      After 7:00 PM is by appointment only.<br>
      Closed only on Thanksgiving &amp; Christmas
    </div>

    <div class="back__cards-label">We Accept All major credit cards:</div>

    <div class="back__badges">
      <span class="badge badge--one"></span>
      <span class="badge badge--two"></span>
      <span class="badge badge--three"></span>
      <span class="badge badge--four"></span>
    </div>

    <div class="back__cash-note">but prefer cash. Thank you</div>
  </section>

</main>
</body>
</html>
```